Re-design web project

Lumen Wafer Systems offers a new range of micro compenents in optic and piezoelectric fields, and respond to specifc R&D requirements for the development of tailored components.

Use informations contained in the actual site (www.lumenwafer-example.com) and redesign the site with a marketing and industrial approach.
The new website should be based on the angosaxon model.

Target Market(s)

We have a target market of people 30 to 60 years old who are industrialists.

Requirements
Must have
• We want an french & english web site, the first page must be in english.
• We imagine a site with a dynamic animated banner, a feedback insert, a newsletter insert with the possibility of suscription and a contact page.
• You must insert a link to friendnest, workmesh and proxilo.
• The design must be compatible with smartphone.
• Itsn't necessary to insert Lumen Wafer's picture. The most important is to have an idea of the design of the website. So you can put in any other picture.
• Of course, the logo is mandatory in the first page.
• Please give us a datasheet explaining how update and modify the website.
Nice to have
• it's nice to have a drop-down menu which explain every application.

```html
<!DOCTYPE html>
<html lang="en">
<head>
<meta charset="utf-8">
<title>Lumen Wafer Systems</title>
<link href="https://fonts.googleapis.com/css2?family=Arimo:wght@400;700&display=swap" rel="stylesheet">
<style>
:root{
  --ink:#111;
  --body:#555;
  --olive:#8a7a00;
  --olive-dark:#4d4600;
  --band:#f3f3f3;
  --rule:#cfcfcf;
  --orange:#ff9a00;
  --footer:#2a2a2a;
  --topbar:#555;
  --navy:#2d3d9a;
}
*{box-sizing:border-box;margin:0;padding:0}
html,body{width:1200px;height:1120px;overflow:hidden;background:#fff;font-family:Arimo,Arial,sans-serif;color:var(--ink)}
.page{position:relative;width:1200px;height:1120px}
.abs{position:absolute}
.topbar{left:0;top:0;width:1200px;height:9px;background:var(--topbar)}
.brand{left:220px;top:44px;display:flex;align-items:center;gap:12px}
.brand-dot{width:44px;height:44px;border-radius:50%;background:#555}
.brand-name{font-size:30px;font-weight:400;color:#555;letter-spacing:.5px}
.lang{left:825px;top:21px;font-size:10px;color:#555}
.lang-box{left:913px;top:14px;width:55px;height:24px;border:1px solid #ccc;background:linear-gradient(#fff,#eee)}
.lang-box span{position:absolute;left:9px;top:7px;width:16px;height:10px;background:linear-gradient(#b22 0 50%,#eee 50%);}
.lang-box i{position:absolute;right:8px;top:10px;border:3px solid transparent;border-top-color:#777}
.nav{left:682px;top:50px;display:flex;font-size:12px;font-weight:700}
.nav a{display:block;height:42px;line-height:40px;padding:0 15px;color:var(--ink);text-decoration:none}
.nav a.active{background:#ddd;border-bottom:4px solid var(--olive-dark)}
.hero{left:0;top:123px;width:1200px;height:318px;background:radial-gradient(ellipse at 45% 40%,#b7834a 0%,#6b4424 40%,#2a1a10 75%,#120b06 100%)}
.hero-title{left:260px;top:246px;font-size:29px;font-weight:700;color:var(--navy);-webkit-text-stroke:1px #fff}
.hero-arrow{top:262px}
.dots{left:585px;top:404px;display:flex;gap:7px}
.dots i{width:10px;height:10px;border-radius:50%;background:#eee;border:1px solid #888}
.dots i.on{background:#5b8fd6}
.intro{left:0;top:441px;width:1200px;height:130px;background:var(--band)}
.intro h2{position:absolute;left:219px;top:20px;font-size:20px;font-weight:400}
.intro p,.about p,.news-item p{font-size:9.6px;line-height:11.8px;color:var(--body)}
.intro p{position:absolute;left:219px;top:56px;width:450px}
.download{left:735px;top:463px}
.dl-btn{left:832px;top:482px;width:154px;height:47px;background:var(--orange);color:#fff;font-size:20px;font-weight:700;line-height:47px;padding-left:12px}
.dl-btn svg{position:absolute;right:12px;top:10px}
.section-title{font-size:17px;font-weight:700}
.about-photo{left:218px;top:627px;width:231px;height:124px;border:1px solid var(--rule);background:#fff}
.about-photo div{position:absolute;left:14px;top:12px;width:202px;height:97px;background:linear-gradient(90deg,#6b4a3a,#3a2a24 45%,#5b4434 80%,#c8b6b8)}
.about h3{position:absolute;left:467px;top:628px;font-size:15px;font-weight:400;color:var(--olive)}
.about p{position:absolute;left:466px;width:505px}
.box{border:1px solid var(--rule);background:#fff;box-shadow:0 1px 2px rgba(0,0,0,.15)}
.news-item{position:absolute;left:8px;width:484px;height:88px}
.news-item .badge{position:absolute;left:14px;top:14px;width:70px;height:62px;background:#eef0f4;border-radius:50%}
.news-item h4{position:absolute;left:114px;top:14px;font-size:11.5px;font-weight:400;line-height:14px;width:300px}
.news-item p{position:absolute;left:114px;top:56px;width:370px}
.news-sep{position:absolute;left:8px;width:484px;border-top:1px dotted #bbb}
.event{position:absolute;left:4px;width:212px;height:74px}
.event .mark{position:absolute;background:#e9e2a8}
.event p{position:absolute;font-size:8.6px;font-weight:700;line-height:10.5px;color:#444}
.footer{left:0;top:1043px;width:1200px;height:77px;background:var(--footer);color:#fff;font-size:10px}
.footer .links{position:absolute;left:218px;top:30px}
.footer .copy{position:absolute;left:478px;top:29px;font-weight:700}
.social{position:absolute;left:908px;top:25px;display:flex;gap:6px}
.social span{display:block;height:22px;line-height:22px;padding:0 7px;border-radius:11px;background:#fff;color:#2a2a2a;font-size:8px;font-weight:700}
</style>
</head>
<body>
<div class="page">
  <div class="abs topbar"></div>

  <header>
    <div class="abs brand"><span class="brand-dot"></span><span class="brand-name">Lumen Wafer Systems</span></div>
    <div class="abs lang">Select Languages :</div>
    <div class="abs lang-box"><span></span><i></i></div>
    <nav class="abs nav">
      <a class="active" href="#">Home</a><a href="#">About</a><a href="#">Applications</a><a href="#">Contact</a>
    </nav>
  </header>

  <section class="abs hero" role="img" aria-label="Close-up photo of glowing micro component grid"></section>
  <div class="abs hero-title">Lumen Wafer Systems</div>
  <svg class="abs hero-arrow" style="left:52px" width="20" height="32" viewBox="0 0 20 32"><path d="M16 3 5 16l11 13" fill="none" stroke="#fff" stroke-width="5"/></svg>
  <svg class="abs hero-arrow" style="left:1114px" width="20" height="32" viewBox="0 0 20 32"><path d="M4 3l11 13L4 29" fill="none" stroke="#fff" stroke-width="5"/></svg>
  <div class="abs dots"><i class="on"></i><i></i><i></i></div>

  <section class="abs intro">
    <h2>Lumen Wafer Presentation</h2>
    <p>Lumen Wafer uses an innovative process to exhibit high coefficients ferroelectric single crystals which is particularly efficient for micro and nanotechnologies devices. We offer a new range of micro components in optic and piezoelectric fields, and respond to your specific R&amp;D requirements for the development of tailored components</p>
  </section>
  <svg class="abs download" width="100" height="72" viewBox="0 0 100 72">
    <path d="M2 10h16l4-6h24v8H96v58H2z" fill="#6e0b0b"/>
    <rect x="2" y="16" width="96" height="54" rx="3" fill="#9d1616"/>
    <rect x="2" y="16" width="96" height="10" fill="#c02424"/>
  </svg>
  <div class="abs dl-btn">Download
    <svg width="28" height="26" viewBox="0 0 28 26"><path d="M10 0h8v10h6L14 20 4 10h6z" fill="#2a1a00"/><path d="M1 17v7h26v-7" fill="none" stroke="#2a1a00" stroke-width="3"/></svg>
  </div>

  <section class="about">
    <h2 class="abs section-title" style="left:219px;top:592px">About Lumen Wafer</h2>
    <div class="abs about-photo"><div role="img" aria-label="Photo of a micro display chip with its PCB interface"></div></div>
    <h3>Development of Innovative Micro Components</h3>
    <p style="top:658px">Lumen Wafer uses an innovative process to exhibit high coefficients ferroelectric single crystals which is particularly efficient for micro and nanotechnologies devices. We offer a new range of micro components in optic and piezoelectric fields, and respond to your specific R&amp;D requirements for the development of tailored components.</p>
    <p style="top:706px">Lumen Wafer's technology leads to a micromassive structure based on a thick film of ferroelectric single crystals, preserving their natural intrinsic properties. We are able to produce thick films with thicknesses from 500µm down to 10µm.</p>
  </section>

  <h2 class="abs section-title" style="left:219px;top:796px">News</h2>
  <svg class="abs" style="left:692px;top:797px" width="30" height="12" viewBox="0 0 30 12"><path d="M6 1 1 6l5 5M19 1l5 5-5 5" fill="none" stroke="#999" stroke-width="2"/></svg>
  <section class="abs box" style="left:218px;top:824px;width:501px;height:199px">
    <div class="news-item" style="top:4px">
      <div class="badge" role="img" aria-label="Innovation contest badge"></div>
      <h4>Award 2012 of National Innovative Company Creation competition : MRIN/INOVA</h4>
      <p>The aim of the National Innovative Company Creation competition is to detect, to help the new entrepreneurs to create innovative company and to develop projects and support the best of them with financial assistance and appropriate support.</p>
    </div>
    <div class="news-sep" style="top:101px"></div>
    <div class="news-item" style="top:94px">
      <div class="badge" style="border-radius:4px" role="img" aria-label="Foundation partner badge"></div>
      <h4>Award 2012 of National Innovative Company Creation competition : MRIN/INOVA</h4>
      <p>The aim of the National Innovative Company Creation competition is to detect, to help the new entrepreneurs to create innovative company and to develop projects and support the best of them with financial assistance and appropriate support.</p>
    </div>
  </section>

  <h2 class="abs section-title" style="left:765px;top:796px">Events</h2>
  <section class="abs box" style="left:766px;top:824px;width:220px;height:199px">
    <div class="event" style="top:6px">
      <div class="mark" style="left:24px;top:6px;width:62px;height:40px" role="img" aria-label="Trade fair badge"></div>
      <p style="left:110px;top:7px">OPTICOM 2012<br>Amsterdam<br>16-20 sept 2012<br>Hall 1 - Booth 421</p>
    </div>
    <div class="news-sep" style="left:4px;width:212px;top:61px"></div>
    <div class="event" style="top:66px">
      <div class="mark" style="left:44px;top:6px;width:30px;height:54px" role="img" aria-label="Optics show badge"></div>
      <p style="left:103px;top:20px">Vitrine Nova<br>Paris, 4-6 Oct 2011<br>Porte de Versailles<br>Hall 7.3</p>
    </div>
    <div class="news-sep" style="left:4px;width:212px;top:143px"></div>
    <div class="mark abs" style="left:19px;top:154px;width:172px;height:32px;background:linear-gradient(90deg,#cfe08a,#fff6c8)" role="img" aria-label="Photonics fair banner"></div>
  </section>

  <footer class="abs footer">
    <div class="links">Home &nbsp;|&nbsp; About &nbsp;|&nbsp; Applications &nbsp;|&nbsp; Contact</div>
    <div class="copy">© 2011 - Lumen Wafer Systems - All rights reserved</div>
    <div class="social"><span>friendnest</span><span>workmesh</span><span>proxilo</span></div>
  </footer>
</div>
</body>
</html>
```